Harbor Total Recovery Tradeshow Booth Design

We need a tradeshow booth design for a 10x20 booth. We are a COMMERCIAL ONLY disaster restoration company focusing on water and flood restoration, fire and smoke remediation, mold and biohazard, structural repair and asset protection.

These are the links to the booth we need graphics designed for. The spec sheets for them are also in the attachments.
https://www.boothvexa.com/Corvina-Helix-Swift-Frame-p/corvina.htm?CartID=2
https://www.boothvexa.com/Tidara-52-Counter-p/tdc-52.htm?CartID=1
https://www.boothvexa.com/6ft-Stretch-Table-Cover-p/tbl-6-stretch.htm?CartID=5

Target Market(s)

Real Estate, Educational Facilities, Hospitality Facilities, Medical Facilities

Industry/Entity Type

Construction

Requirements
Must have
• Our logo. The colors from the attached presentation. Pictures of COMMERCIAL ONLY facilities and losses (can use some from attached presentation). Our services (water and flood, fire and smoke, mold and biohazard, structural repair, asset protection). Our slogan (Exceeding your expectations when you need it most).
Nice to have
• Include the above
Should not have
• Do not include anything residential looking at all (no pictures). Do not include the case studies on the pictures.

```html
<!DOCTYPE html>
<html lang="en">
<head>
<meta charset="utf-8">
<title>Harbor Total Recovery – Booth Graphics</title>
<link href="https://fonts.googleapis.com/css2?family=Ubuntu:wght@400;500;700&family=Ubuntu+Condensed&display=swap" rel="stylesheet">
<style>
  :root{
    --orange:#ee7430;
    --navy:#1f3a45;
    --navy-deep:#1c323b;
    --teal:#3b6b7b;
    --sky:#72afc6;
    --white:#ffffff;
    --page:#ffffff;
  }
  *{box-sizing:border-box;margin:0;padding:0}
  html,body{width:1200px;height:846px;overflow:hidden;background:var(--page)}
  body{font-family:"Ubuntu",sans-serif}
  .booth{position:absolute;left:14px;top:193px;display:flex;gap:6px;height:460px}
  .panel{position:relative;height:460px;overflow:hidden}
  .panel > svg.bg{position:absolute;inset:0;width:100%;height:100%}
  .wide{width:220px}
  .main{width:216px}
  .narrow{width:66px}
  .services{width:132px;background:var(--navy-deep);text-align:center;font-family:"Ubuntu Condensed",sans-serif}

  .url{position:absolute;top:13px;left:0;right:0;text-align:center;color:var(--navy);font-size:16px;white-space:nowrap}
  .photo{position:absolute}
  .photo-round{border:5px solid var(--white);border-radius:50%;width:140px;height:140px}
  .photo-oval{border:3px solid var(--white);border-radius:50%;width:50px;height:112px;left:8px;top:325px}
  .arena{background:radial-gradient(circle at 50% 35%,#4b5a75,#c4b89a 70%,#8e7d62)}
  .aerial-flood{background:linear-gradient(170deg,#8897a4 0%,#6f7f6a 35%,#8c7355 60%,#4d5f3d 100%);clip-path:polygon(0 0,100% 27%,100% 100%,0 100%);left:0;top:237px;width:220px;height:223px}
  .city-flood{background:linear-gradient(180deg,#d8dcdf 0%,#9a9893 40%,#6c5148 55%,#55595a 100%);clip-path:polygon(0 27%,100% 0,100% 100%,0 100%);left:0;top:237px;width:220px;height:223px}
  .warehouse{background:radial-gradient(circle at 40% 40%,#8a7a6a,#2e2a28 75%)}
  .corridor{background:radial-gradient(circle at 50% 40%,#e8e2d6,#a99075 65%,#6e5a48)}
  .flooded-lot{background:linear-gradient(180deg,#6e8aa0 0%,#5c7a52 35%,#c9a66a 60%,#b99256 100%)}
  .gym-floor{background:linear-gradient(180deg,#d6d8e2,#b48a5c 50%,#2c4e8a)}
  .dark-water{background:linear-gradient(180deg,#25282a,#4f5254 60%,#7a7e80)}

  .brand{position:absolute;top:20px;left:6px;right:6px;text-align:center;color:var(--orange);font-weight:700;font-size:23px;line-height:1.05;text-transform:uppercase;white-space:nowrap}
  .slogan{position:absolute;left:-20px;right:-20px;top:160px;text-align:center;color:var(--white);font-size:14px;line-height:1.2;white-space:nowrap}
  .slogan-up{transform:rotate(-20deg)}
  .slogan-down{transform:rotate(20deg)}
  .photo-main{left:38px;top:270px}

  .side-title{position:absolute;top:6px;left:2px;right:2px;color:var(--navy);font-family:"Ubuntu Condensed",sans-serif;font-size:7px;line-height:1.3;text-transform:uppercase;white-space:nowrap;letter-spacing:-.1px}
  .side-title.right{text-align:center}
  .bucket-list{position:absolute;top:82px;left:3px;right:2px;list-style:none;color:var(--white);font-family:"Ubuntu Condensed",sans-serif;font-size:5.4px;line-height:1.55}
  .bucket-list li{padding-left:4px;text-indent:-4px}
  .bucket-list li::before{content:"• "}
  .industry-list{position:absolute;top:66px;left:5px;right:2px;list-style:none;color:var(--white);font-family:"Ubuntu Condensed",sans-serif;font-size:6px;white-space:nowrap}
  .industry-list li{display:flex;align-items:center;gap:3px;height:36px}
  .industry-list svg{width:9px;height:9px;flex:none;fill:var(--orange)}

  .services h2{color:var(--orange);font-weight:400;font-size:16px;margin-top:22px;white-space:nowrap}
  .service-list{list-style:none;margin-top:10px}
  .service-list li{color:var(--white);font-size:20px;line-height:1.2;padding:12px 0 13px;margin:0 14px;border-bottom:1px solid var(--orange)}
  .service-list li:last-child{border-bottom:none}
  .services .closing{color:var(--orange);font-size:16px;line-height:1.35;margin-top:14px;white-space:nowrap}
</style>
</head>
<body>
<main class="booth">

  <section class="panel wide">
    <svg class="bg" viewBox="0 0 220 460" preserveAspectRatio="none" aria-hidden="true">
      <rect width="220" height="460" fill="var(--orange)"/>
      <polygon points="0,95 220,45 220,460 0,460" fill="var(--navy)"/>
      <polygon points="0,225 220,285 220,297 0,237" fill="var(--white)"/>
    </svg>
    <p class="url">harbortotalrecovery.com</p>
    <div class="photo photo-round arena" style="left:38px;top:68px" role="img" aria-label="Photo: flooded commercial arena floor with restoration crew"></div>
    <div class="photo aerial-flood" role="img" aria-label="Photo: aerial view of a flooded city district"></div>
  </section>

  <section class="panel narrow">
    <svg class="bg" viewBox="0 0 66 460" preserveAspectRatio="none" aria-hidden="true">
      <rect width="66" height="460" fill="var(--navy)"/>
      <polygon points="0,0 66,0 66,15 0,78" fill="var(--orange)"/>
      <polygon points="0,305 66,280 66,460 0,460" fill="var(--sky)"/>
      <polygon points="0,297 66,272 66,280 0,305" fill="var(--white)"/>
    </svg>
    <h3 class="side-title">The Harbor<br>Bucket</h3>
    <ul class="bucket-list">
      <li>Exclusively Pre-established Relationships</li>
      <li>Operational Efficiency Centered Around Internal Resources</li>
      <li>We do not Subscribe to ANY Insurance Program Work</li>
      <li>All Commercial Work</li>
      <li>Business Plan Centered Around Consistency, Reputation and the Expectation of Excellence...Regardless of the Situation</li>
    </ul>
    <div class="photo photo-oval gym-floor" role="img" aria-label="Photo: water-damaged gymnasium floor"></div>
  </section>

  <section class="panel main">
    <svg class="bg" viewBox="0 0 216 460" preserveAspectRatio="none" aria-hidden="true">
      <rect width="216" height="460" fill="var(--teal)"/>
      <polygon points="0,258 216,163 216,175 0,270" fill="var(--white)"/>
      <polygon points="0,270 216,175 216,460 0,460" fill="var(--sky)"/>
    </svg>
    <h1 class="brand">Harbor Total<br>Recovery</h1>
    <p class="slogan slogan-up">Exceeding your expectations<br>when you need it most</p>
    <div class="photo photo-round photo-main corridor" role="img" aria-label="Photo: technicians in protective suits in a commercial corridor"></div>
  </section>

  <section class="panel services">
    <h2>OUR SERVICES</h2>
    <ul class="service-list">
      <li>water and<br>flood</li>
      <li>fire and<br>smoke</li>
      <li>mold and<br>biohazard</li>
      <li>structural<br>repair</li>
    </ul>
    <p class="closing">ASSET<br>PROTECTION</p>
  </section>

  <section class="panel main">
    <svg class="bg" viewBox="0 0 216 460" preserveAspectRatio="none" aria-hidden="true">
      <rect width="216" height="460" fill="var(--teal)"/>
      <polygon points="0,163 216,258 216,270 0,175" fill="var(--white)"/>
      <polygon points="0,175 216,270 216,460 0,460" fill="var(--sky)"/>
    </svg>
    <h2 class="brand">Harbor Total<br>Recovery</h2>
    <p class="slogan slogan-down">Exceeding your expectations<br>when you need it most</p>
    <div class="photo photo-round photo-main flooded-lot" role="img" aria-label="Photo: flooded commercial building plaza"></div>
  </section>

  <section class="panel narrow">
    <svg class="bg" viewBox="0 0 66 460" preserveAspectRatio="none" aria-hidden="true">
      <rect width="66" height="460" fill="var(--navy)"/>
      <polygon points="0,0 66,0 66,78 0,36" fill="var(--orange)"/>
      <polygon points="0,280 66,305 66,460 0,460" fill="var(--sky)"/>
      <polygon points="0,272 66,297 66,305 0,280" fill="var(--white)"/>
    </svg>
    <h3 class="side-title right">Specialization<br>of Industries</h3>
    <ul class="industry-list">
      <li><svg viewBox="0 0 10 10"><path d="M4 0h2v4h4v2H6v4H4V6H0V4h4z"/></svg>Medical</li>
      <li><svg viewBox="0 0 10 10"><path d="M5 0l5 4v6H0V4z"/></svg>Hospitality</li>
      <li><svg viewBox="0 0 10 10"><rect x="1" y="0" width="8" height="10"/></svg>Educational</li>
      <li><svg viewBox="0 0 10 10"><path d="M4.3 0h1.4v3.5L10 6v1.2L5.7 6v2.5L7 9.5V10L5 9.4 3 10v-.5l1.3-1V6L0 7.2V6l4.3-2.5z"/></svg>Airports</li>
      <li><svg viewBox="0 0 10 10"><path d="M1 2h8v8H1zM3 0h4v2H3z"/></svg>Office/Industrial</li>
      <li><svg viewBox="0 0 10 10"><path d="M0 0h5l5 5-5 5-5-5z"/></svg>Retail</li>
    </ul>
    <div class="photo photo-oval dark-water" role="img" aria-label="Photo: standing water inside a dark commercial space"></div>
  </section>

  <section class="panel wide">
    <svg class="bg" viewBox="0 0 220 460" preserveAspectRatio="none" aria-hidden="true">
      <rect width="220" height="460" fill="var(--orange)"/>
      <polygon points="0,45 220,95 220,460 0,460" fill="var(--navy)"/>
      <polygon points="0,285 220,225 220,237 0,297" fill="var(--white)"/>
    </svg>
    <p class="url">harbortotalrecovery.com</p>
    <div class="photo photo-round warehouse" style="left:42px;top:72px" role="img" aria-label="Photo: damaged interior of a commercial warehouse"></div>
    <div class="photo city-flood" role="img" aria-label="Photo: flooded downtown commercial buildings"></div>
  </section>

</main>
</body>
</html>
```